I need someone to help me finish my logo for Tarvell Honey and create a honey label template I can use and amend for each harvest.
I created some basic labels last year but I want the quality to be better as my partner made the logo in Word. I also want a label with more detail so I can sell the honey to local shops e.g. include nutritionals, ingredients, address. Visit tarvellhoney on instagram to see more and examples of last years label in situ.

```html
<!DOCTYPE html>
<html lang="en">
<head>
<meta charset="utf-8">
<title>Tarvell Honey – Label Options</title>
<link href="https://fonts.googleapis.com/css2?family=Heebo:wght@300;400&display=swap" rel="stylesheet">
<style>
  :root {
    --board: #e3e3e3;
    --label: #ffffff;
    --ink: #1e1e1e;
    --ink-soft: #555555;
    --purple: #7b3d96;
    --purple-deep: #4e2466;
    --purple-light: #c9a6cf;
    --rule: #1e1e1e;
  }
  * { box-sizing: border-box; margin: 0; padding: 0; }
  html, body { width: 1080px; height: 1200px; overflow: hidden; }
  body { background: var(--board); font-family: "Heebo", sans-serif; color: var(--ink); position: relative; }

  .label { position: absolute; left: 132px; width: 813px; height: 342px; background: var(--label); overflow: hidden; }
  .label--purple { top: 43px; }
  .label--line { top: 428px; }
  .label--plain { top: 815px; }

  .back-title { position: absolute; left: 0; width: 324px; top: 18px; text-align: center; font-weight: 300; font-size: 23px; letter-spacing: 0.5px; line-height: 1; }
  .back-tagline { position: absolute; left: 0; width: 324px; top: 44px; text-align: center; font-weight: 300; font-size: 6.5px; color: var(--ink-soft); letter-spacing: 0.3px; }
  .label--purple .back-tagline { color: var(--purple); }
  .back-description { position: absolute; left: 56px; top: 59px; font-weight: 300; font-size: 10px; line-height: 12.6px; color: var(--ink-soft); }

  .nutrition { position: absolute; left: 104px; top: 98px; width: 116px; font-weight: 300; }
  .nutrition-title { font-size: 15px; line-height: 1; font-weight: 300; }
  .nutrition-serving { font-size: 5px; margin-top: 1px; padding-bottom: 4px; border-bottom: 2px solid var(--rule); }
  .nutrition-row { display: flex; justify-content: space-between; font-size: 5px; line-height: 8.6px; border-bottom: 0.6px solid var(--rule); font-weight: 400; }
  .nutrition-row--sub { padding-left: 6px; font-weight: 300; }
  .nutrition-row--calories { border-bottom-width: 2px; }
  .nutrition-row--dv { justify-content: flex-end; font-size: 4px; line-height: 7px; font-weight: 300; }
  .nutrition-row--last { border-bottom-width: 2px; }
  .nutrition-note { font-size: 3.6px; margin-top: 2px; font-weight: 300; }

  .back-origin { position: absolute; left: 56px; top: 257px; font-weight: 300; font-size: 10.5px; color: var(--ink-soft); }
  .back-social { position: absolute; left: 165px; top: 254px; display: flex; align-items: center; gap: 5px; font-weight: 300; font-size: 12.5px; color: var(--ink); }
  .label--purple .back-social { color: var(--purple); }
  .social-dot { width: 16px; height: 16px; border: 1px solid currentColor; border-radius: 50%; }

  .front-illustration { position: absolute; left: 475px; top: 52px; width: 205px; height: 142px; background: linear-gradient(135deg, #f4f4f4, #e2e2e2); }
  .front-name { position: absolute; left: 578px; top: 186px; font-weight: 300; font-size: 37px; line-height: 1; letter-spacing: 0.5px; color: var(--ink); }
  .front-tagline { position: absolute; left: 578px; width: 150px; top: 223px; text-align: center; font-weight: 300; font-size: 13px; color: var(--purple); letter-spacing: 0.4px; }
  .front-weight { position: absolute; left: 516px; top: 281px; font-weight: 300; font-size: 19px; color: var(--ink); }
  .label--purple .front-weight { color: var(--purple); }
  .label--plain .front-weight { left: 476px; top: 303px; }

  .band { position: absolute; left: 0; bottom: 0; width: 813px; height: 72px; display: block; }
</style>
</head>
<body>

<!-- Label option: purple faceted band -->
<section class="label label--purple">
  <h1 class="back-title">TARVELL</h1>
  <p class="back-tagline">PURE RAW HONEY</p>
  <p class="back-description">Pure, raw and unfiltered honey harvested from<br>Tarvell hives in Wattle Ridge and Kellmore NSW.</p>
  <div class="nutrition">
    <h2 class="nutrition-title">Nutrition Facts</h2>
    <p class="nutrition-serving">Serving Size 1 Tbsp (21g)</p>
    <div class="nutrition-row"><span>Amount Per Serving</span></div>
    <div class="nutrition-row nutrition-row--calories"><span>Calories 60</span></div>
    <div class="nutrition-row nutrition-row--dv"><span>% Daily Values*</span></div>
    <div class="nutrition-row"><span>Total Fat 0g</span><span>0%</span></div>
    <div class="nutrition-row nutrition-row--sub"><span>Saturated Fat 0g</span><span>0%</span></div>
    <div class="nutrition-row nutrition-row--sub"><span>Trans Fat 0g</span><span>0%</span></div>
    <div class="nutrition-row"><span>Sodium 0mg</span><span>0%</span></div>
    <div class="nutrition-row"><span>Total Carbohydrate 17g</span><span>6%</span></div>
    <div class="nutrition-row nutrition-row--sub"><span>Dietary Fiber 0g</span><span>0%</span></div>
    <div class="nutrition-row nutrition-row--sub"><span>Sugars 16g</span><span></span></div>
    <div class="nutrition-row nutrition-row--last"><span>Protein 0g</span><span>0%</span></div>
    <p class="nutrition-note">*Percent Daily Values are based on a 2,000 calorie diet.</p>
  </div>
  <p class="back-origin">Sydney Australia</p>
  <p class="back-social"><span class="social-dot"></span>@tarvellhoney</p>
  <div class="front-illustration" role="img" aria-label="Geometric line illustration of a honey bee in flight"></div>
  <p class="front-name">TARVELL</p>
  <p class="front-tagline">PURE RAW HONEY</p>
  <p class="front-weight">350gr</p>
  <svg class="band" viewBox="0 0 813 72" preserveAspectRatio="none" role="img" aria-label="Faceted purple geometric mountain pattern">
    <defs>
      <linearGradient id="bandPurple" x1="0" y1="0" x2="1" y2="0">
        <stop offset="0" stop-color="#5a2a72"/>
        <stop offset="0.3" stop-color="#a883b4"/>
        <stop offset="0.6" stop-color="#7b3d96"/>
        <stop offset="1" stop-color="#8c5aa4"/>
      </linearGradient>
    </defs>
    <polygon fill="url(#bandPurple)" points="0,0 76,3 169,50 228,3 330,45 435,36 523,60 623,8 689,9 813,0 813,72 0,72"/>
  </svg>
</section>

<!-- Label option: line-work band -->
<section class="label label--line">
  <h1 class="back-title">TARVELL</h1>
  <p class="back-tagline">PURE RAW HONEY</p>
  <p class="back-description">Pure, raw and unfiltered honey harvested from<br>Tarvell hives in Wattle Ridge and Kellmore NSW.</p>
  <div class="nutrition">
    <h2 class="nutrition-title">Nutrition Facts</h2>
    <p class="nutrition-serving">Serving Size 1 Tbsp (21g)</p>
    <div class="nutrition-row"><span>Amount Per Serving</span></div>
    <div class="nutrition-row nutrition-row--calories"><span>Calories 60</span></div>
    <div class="nutrition-row nutrition-row--dv"><span>% Daily Values*</span></div>
    <div class="nutrition-row"><span>Total Fat 0g</span><span>0%</span></div>
    <div class="nutrition-row nutrition-row--sub"><span>Saturated Fat 0g</span><span>0%</span></div>
    <div class="nutrition-row nutrition-row--sub"><span>Trans Fat 0g</span><span>0%</span></div>
    <div class="nutrition-row"><span>Sodium 0mg</span><span>0%</span></div>
    <div class="nutrition-row"><span>Total Carbohydrate 17g</span><span>6%</span></div>
    <div class="nutrition-row nutrition-row--sub"><span>Dietary Fiber 0g</span><span>0%</span></div>
    <div class="nutrition-row nutrition-row--sub"><span>Sugars 16g</span><span></span></div>
    <div class="nutrition-row nutrition-row--last"><span>Protein 0g</span><span>0%</span></div>
    <p class="nutrition-note">*Percent Daily Values are based on a 2,000 calorie diet.</p>
  </div>
  <p class="back-origin">Sydney Australia</p>
  <p class="back-social"><span class="social-dot"></span>@tarvellhoney</p>
  <div class="front-illustration" role="img" aria-label="Geometric line illustration of a honey bee in flight"></div>
  <p class="front-name">TARVELL</p>
  <p class="front-tagline">PURE RAW HONEY</p>
  <p class="front-weight">350gr</p>
  <svg class="band" viewBox="0 0 813 72" preserveAspectRatio="none" role="img" aria-label="Black line-work geometric mountain pattern">
    <defs>
      <linearGradient id="bandLine" x1="0" y1="0" x2="0" y2="1">
        <stop offset="0" stop-color="#ffffff"/>
        <stop offset="1" stop-color="#ececec"/>
      </linearGradient>
    </defs>
    <polygon fill="url(#bandLine)" points="0,0 76,3 169,50 228,3 330,45 435,36 523,60 623,8 689,9 813,0 813,72 0,72"/>
  </svg>
</section>

<!-- Label option: plain -->
<section class="label label--plain">
  <h1 class="back-title">TARVELL</h1>
  <p class="back-tagline">PURE RAW HONEY</p>
  <p class="back-description">Pure, raw and unfiltered honey harvested from<br>Tarvell hives in Wattle Ridge and Kellmore NSW.</p>
  <div class="nutrition">
    <h2 class="nutrition-title">Nutrition Facts</h2>
    <p class="nutrition-serving">Serving Size 1 Tbsp (21g)</p>
    <div class="nutrition-row"><span>Amount Per Serving</span></div>
    <div class="nutrition-row nutrition-row--calories"><span>Calories 60</span></div>
    <div class="nutrition-row nutrition-row--dv"><span>% Daily Values*</span></div>
    <div class="nutrition-row"><span>Total Fat 0g</span><span>0%</span></div>
    <div class="nutrition-row nutrition-row--sub"><span>Saturated Fat 0g</span><span>0%</span></div>
    <div class="nutrition-row nutrition-row--sub"><span>Trans Fat 0g</span><span>0%</span></div>
    <div class="nutrition-row"><span>Sodium 0mg</span><span>0%</span></div>
    <div class="nutrition-row"><span>Total Carbohydrate 17g</span><span>6%</span></div>
    <div class="nutrition-row nutrition-row--sub"><span>Dietary Fiber 0g</span><span>0%</span></div>
    <div class="nutrition-row nutrition-row--sub"><span>Sugars 16g</span><span></span></div>
    <div class="nutrition-row nutrition-row--last"><span>Protein 0g</span><span>0%</span></div>
    <p class="nutrition-note">*Percent Daily Values are based on a 2,000 calorie diet.</p>
  </div>
  <p class="back-origin">Sydney Australia</p>
  <p class="back-social"><span class="social-dot"></span>@tarvellhoney</p>
  <div class="front-illustration" role="img" aria-label="Geometric line illustration of a honey bee in flight"></div>
  <p class="front-name">TARVELL</p>
  <p class="front-tagline">PURE RAW HONEY</p>
  <p class="front-weight">350gr</p>
</section>

</body>
</html>
```